Harbourline Service Allies Wordpress Design

See attached brief. If you have questions beyond this please let me know. Brief document is HS Allies Website Design v1. Other documents are files from logo creation and business cards to give you an idea of colours and images. Also see document that shows examples of the types of images I want to display on the website.

Focus of site is for customers and to drive traffic from social media etc. Company is startup consulting business in Customer Experience and Contact Centre. We offer benchmarking, strategy reviews, technology audits. etc

Looking for the site to use the existing Wordpress theme on hostNest or something compatible. Happy to change if there is a good reason for doing so.

Has to be easy to manage ongoing if possible.

Target Market(s)

HSA is a consulting organisation in contact centre and customer experience

Number of Pages Required

4 page

Font styles to use
Serif
Sans Serif

Colors
0255a3
3276b5
33a6d7
0293ce
ffffff
fefdec

Requirements
Must have
• Hosted on hostNest so must be compatible. Preference is to use the theme that is already there (Lumeo) unless there is a reason not to
Nice to have
• see brief

```html
<!DOCTYPE html>
<html lang="en">
<head>
<meta charset="utf-8">
<title>Harbourline Service Allies</title>
<link href="https://fonts.googleapis.com/css2?family=Cinzel:wght@400;700&family=Lato:wght@400;700&display=swap" rel="stylesheet">
<style>
:root{
  --navy:#0255a3;
  --mid:#3276b5;
  --sky:#33a6d7;
  --cyan:#0293ce;
  --white:#ffffff;
  --cream:#fefdec;
  --ink:#2b2b2b;
  --text:#555;
  --grey-band:#e4e4e4;
  --footer:#0b4c8c;
  --serif:'Cinzel', Georgia, serif;
  --sans:'Lato', Arial, sans-serif;
}
*{box-sizing:border-box;margin:0;padding:0}
html,body{width:1200px;height:2663px;overflow:hidden;background:var(--white)}
body{font-family:var(--sans);color:var(--ink)}
.page{position:relative;width:1200px;height:2663px;overflow:hidden}
.abs{position:absolute}

/* header */
.site-header{position:absolute;left:0;top:0;width:1200px;height:107px;background:var(--white);z-index:3}
.brand-tab{position:absolute;left:125px;top:0;width:360px;height:132px;background:var(--white);border-radius:0 0 18px 18px;box-shadow:0 3px 6px rgba(0,0,0,.15);display:flex;flex-direction:column;align-items:center;justify-content:center;gap:4px}
.brand-mark{font-family:var(--serif);font-weight:700;font-size:46px;color:var(--navy);line-height:1}
.brand-name{font-family:var(--serif);font-weight:700;font-size:19px;color:var(--navy);letter-spacing:.5px}
.phone{position:absolute;left:900px;top:18px;display:flex;align-items:center;gap:10px;font-size:19px;color:var(--ink)}
.main-nav{position:absolute;top:66px;left:560px;display:flex;font-family:var(--serif);font-size:16px}
.main-nav a{color:var(--ink);text-decoration:none;padding:0 14px;border-left:1px solid #ccc;line-height:20px}
.main-nav a:first-child{border:0;color:var(--mid);border-bottom:3px solid var(--mid);padding-bottom:7px}

/* hero */
.hero{position:absolute;left:0;top:107px;width:1200px;height:470px;background:linear-gradient(100deg,#3a3a3a 0%,#6d6d6d 35%,#4b4b4b 70%,#2a2a2a 100%)}
.hero-arrow{position:absolute;top:200px;width:38px;height:38px;border-radius:50%;background:rgba(255,255,255,.75);display:flex;align-items:center;justify-content:center}
.hero-caption{position:absolute;left:0;bottom:0;width:1200px;height:112px;background:rgba(0,0,0,.82);color:var(--white);font-family:var(--serif);font-size:30px;text-align:center;line-height:38px;padding-top:18px;letter-spacing:1px}

/* section headings */
.section-title{position:absolute;left:0;width:1200px;text-align:center;font-family:var(--serif);font-size:27px;color:var(--ink)}
.section-title span{color:var(--mid)}
.title-rule{position:absolute;left:50%;transform:translateX(-50%);width:530px;height:1px;background:#cfcfcf}
.title-dot{position:absolute;left:50%;transform:translate(-50%,-50%);width:14px;height:14px;background:var(--mid);border-radius:50%;border:3px solid var(--white)}

/* welcome */
.welcome-title{display:flex;justify-content:center;align-items:center;gap:14px}
.welcome-title .mini{font-weight:700;color:var(--navy);font-size:28px}
.welcome-text{position:absolute;left:142px;top:688px;width:916px;font-size:14.5px;line-height:22px;color:var(--text);text-align:center}
.read-more{position:absolute;left:0;width:1200px;top:798px;text-align:center;font-size:15px;font-weight:700;color:var(--ink);text-decoration:underline}

/* services */
.services{position:absolute;left:0;top:852px;width:1200px;height:440px;background:var(--grey-band)}
.notch{position:absolute;left:588px;width:0;height:0;border-left:14px solid transparent;border-right:14px solid transparent}
.service-card{position:absolute;top:140px;width:222px;height:247px;background:var(--white);border-radius:5px;text-align:center}
.service-card.active{background:var(--mid);color:var(--white)}
.service-icon{position:absolute;left:73px;top:15px;width:76px;height:76px;border-radius:50%;border:3px solid var(--navy);background:var(--white);display:flex;align-items:center;justify-content:center}
.service-icon i{width:60px;height:60px;border-radius:50%;background:var(--navy);display:flex;align-items:center;justify-content:center}
.service-name{position:absolute;top:110px;left:0;width:100%;font-family:var(--serif);font-size:15px;line-height:20px;color:var(--ink)}
.service-card.active .service-name,.service-card.active .service-text{color:var(--white)}
.service-text{position:absolute;top:163px;left:15px;width:192px;font-size:14px;line-height:22px;color:var(--text)}
.carousel-arrow{position:absolute;top:262px}

/* process */
.process-list{position:absolute;list-style:none;font-size:13.5px;font-weight:700;line-height:21px;color:var(--ink);text-transform:uppercase}
.process-list li{position:relative;padding-left:18px}
.process-list li::before{content:"\2713";position:absolute;left:0;font-size:11px;color:#777}
.q-label{position:absolute;width:110px;text-align:center;font-size:14px;font-weight:700;line-height:21px;text-transform:uppercase}

/* result */
.result{position:absolute;left:0;top:1940px;width:1200px;height:424px;background:linear-gradient(180deg,#ececec 0%,#f4f4f4 50%,#e6e6e6 100%)}
.bar{position:absolute;left:559px;width:510px;height:37px;background:rgba(255,255,255,.85)}
.bar b{position:absolute;left:0;top:0;height:37px;color:var(--white);font-size:15px;font-weight:700;line-height:37px;padding-left:16px;white-space:nowrap}

/* footer */
.site-footer{position:absolute;left:0;top:2364px;width:1200px;height:254px;background:var(--footer);color:var(--white)}
.foot-head{position:absolute;top:30px;font-size:16px;font-weight:700}
.foot-links{position:absolute;left:133px;top:68px;list-style:none;font-size:13.5px;line-height:29px}
.foot-links li::before{content:"\203A";margin-right:12px}
.contact-row{position:absolute;left:293px;display:flex;gap:12px;font-size:13px;line-height:18px}
.tweet{position:absolute;left:580px;display:flex;gap:12px;font-size:13px;line-height:18px}
.tweet .avatar{width:42px;height:42px;background:#7e9cbc;flex:none}
.tweet time{display:block;text-align:right}
.foot-divider{position:absolute;left:864px;top:30px;width:1px;height:200px;background:rgba(255,255,255,.2)}
.foot-brand{position:absolute;left:864px;top:40px;width:336px;text-align:center;font-weight:700;font-size:70px;color:rgba(255,255,255,.25);font-family:var(--sans)}
.follow{position:absolute;left:864px;top:146px;width:336px;text-align:center;font-size:17px;font-weight:700}
.socials{position:absolute;left:898px;top:178px;display:flex;gap:11px}
.socials span{width:30px;height:30px;border-radius:50%;background:var(--white)}
.socials span:first-child{background:var(--cyan)}
.copyright{position:absolute;left:0;top:2618px;width:1200px;height:45px;background:var(--cyan);color:var(--white);text-align:center;line-height:45px;font-size:13.5px}
</style>
</head>
<body>
<div class="page">

  <header class="site-header">
    <div class="brand-tab">
      <div class="brand-mark">HSA</div>
      <div class="brand-name">Harbourline Service Allies</div>
    </div>
    <div class="phone">
      <svg width="26" height="26" viewBox="0 0 26 26"><circle cx="13" cy="13" r="12" fill="none" stroke="#2b2b2b" stroke-width="2"/><path d="M9 7c1 0 2 2 2 3s-1 1-1 2c1 2 2 3 4 4 1 0 1-1 2-1s3 1 3 2-2 3-3 3C11 20 6 15 6 10c0-1 2-3 3-3z" fill="#2b2b2b"/></svg>
      (555) 318 2046
    </div>
    <nav class="main-nav">
      <a>Home</a><a>Services</a><a>Partners</a><a>Blog</a><a>Get in Touch</a>
    </nav>
  </header>

  <section class="hero" role="img" aria-label="Photo of a consultant's hand sketching a business diagram of function, marketing and customer ideas">
    <div class="hero-arrow" style="left:45px"><svg width="14" height="14" viewBox="0 0 14 14"><path d="M9 2 4 7l5 5" fill="none" stroke="#333" stroke-width="2.5"/></svg></div>
    <div class="hero-arrow" style="left:1110px"><svg width="14" height="14" viewBox="0 0 14 14"><path d="m5 2 5 5-5 5" fill="none" stroke="#333" stroke-width="2.5"/></svg></div>
    <div class="hero-caption">We are a consulting organisation in contact<br>center and customer experience</div>
  </section>

  <section class="welcome">
    <h1 class="section-title welcome-title" style="top:608px;font-weight:400;font-size:25px"><span class="mini">HSA</span>Welcome to&nbsp;<span>Harbourline Service Allies</span></h1>
    <div class="title-rule" style="top:660px;width:830px"></div>
    <div class="title-dot" style="top:660px"></div>
    <p class="welcome-text">Lorem ipsum dolor sit amet, consectetuer adipiscing elit, sed diam nonummy nibh euismod tincidunt ut laoreet dolore magna aliquam erat volutpat. Ut wisi enim ad minim veniam, quis nostrud exerci tation ullamcorper suscipit lobortis nisl ut aliquip ex ea commodo consequat. Duis autem vel eum iriure dolor in hendrerit in vulputate velit esse molestie consequat, vel illum dolore eu feugiat nulla facilisis at vero eros et accumsan et iusto odio dignissim qui blandit praesent luptatum zzril delenit augue duis dolore te feugait nulla facilisi.</p>
    <a class="read-more">Read More &raquo;</a>
  </section>

  <section class="services">
    <div class="notch" style="top:0;border-top:14px solid var(--white)"></div>
    <h2 class="section-title" style="top:50px;font-weight:400">Our <span>Services</span></h2>
    <div class="title-rule" style="top:102px"></div>
    <div class="title-dot" style="top:102px"></div>

    <svg class="carousel-arrow" style="left:82px" width="20" height="34" viewBox="0 0 20 34"><path d="M17 2 3 17l14 15" fill="none" stroke="#888" stroke-width="3"/></svg>
    <svg class="carousel-arrow" style="left:1090px" width="20" height="34" viewBox="0 0 20 34"><path d="m3 2 14 15L3 32" fill="none" stroke="#888" stroke-width="3"/></svg>

    <article class="service-card" style="left:131px">
      <div class="service-icon"><i><svg width="30" height="26" viewBox="0 0 30 26"><path d="M2 24h26" stroke="#fff" stroke-width="2"/><rect x="4" y="16" width="4" height="7" fill="#fff"/><rect x="11" y="12" width="4" height="11" fill="#fff"/><rect x="18" y="8" width="4" height="15" fill="#fff"/><path d="M4 11 12 5l5 3 9-7" fill="none" stroke="#fff" stroke-width="2"/></svg></i></div>
      <h3 class="service-name">Strategic Operational<br>Review</h3>
      <p class="service-text">Lorem ipsum dolor sit amet consectetuer adipiscing elit sed diam nonummy</p>
    </article>
    <article class="service-card active" style="left:369px">
      <div class="service-icon"><i><svg width="30" height="28" viewBox="0 0 30 28"><rect x="12" y="1" width="6" height="6" fill="#fff"/><rect x="2" y="20" width="6" height="6" fill="#fff"/><rect x="12" y="20" width="6" height="6" fill="#fff"/><rect x="22" y="20" width="6" height="6" fill="#fff"/><path d="M15 7v13M5 20v-6h20v6" fill="none" stroke="#fff" stroke-width="2"/></svg></i></div>
      <h3 class="service-name">Contact Centre<br>Benchmarking</h3>
      <p class="service-text">Lorem ipsum dolor sit amet consectetuer adipiscing elit sed diam nonummy</p>
    </article>
    <article class="service-card" style="left:609px">
      <div class="service-icon"><i><svg width="30" height="30" viewBox="0 0 30 30"><circle cx="15" cy="15" r="11" fill="none" stroke="#fff" stroke-width="2"/><rect x="9" y="15" width="3" height="6" fill="#fff"/><rect x="14" y="11" width="3" height="10" fill="#fff"/><rect x="19" y="13" width="3" height="8" fill="#fff"/></svg></i></div>
      <h3 class="service-name">Caller Intent<br>Analysis</h3>
      <p class="service-text">Lorem ipsum dolor sit amet consectetuer adipiscing elit sed diam nonummy</p>
    </article>
    <article class="service-card" style="left:847px">
      <div class="service-icon"><i><svg width="32" height="28" viewBox="0 0 32 28"><path d="M8 20a6 6 0 0 1 0-12 8 8 0 0 1 15-1 6 6 0 0 1 1 13z" fill="none" stroke="#fff" stroke-width="2"/><path d="m11 14 4 4 7-7" fill="none" stroke="#fff" stroke-width="2"/></svg></i></div>
      <h3 class="service-name">Cloud Readiness<br>Assessment</h3>
      <p class="service-text">Lorem ipsum dolor sit amet consectetuer adipiscing elit sed diam nonummy</p>
    </article>
    <div class="notch" style="top:440px;border-top:14px solid var(--grey-band)"></div>
  </section>

  <section class="process">
    <h2 class="section-title" style="top:1340px;font-weight:400">Our <span>Process</span></h2>
    <div class="title-rule" style="top:1392px"></div>

    <svg class="abs" style="left:0;top:1392px" width="1200" height="548" viewBox="0 0 1200 548">
      <line x1="600" y1="0" x2="600" y2="540" stroke="#d5d5d5" stroke-width="2"/>
      <line x1="165" y1="266" x2="1033" y2="266" stroke="#d5d5d5" stroke-width="2"/>
      <circle cx="600" cy="0" r="7" fill="#3276b5" stroke="#fff" stroke-width="3"/>
      <g fill="none" stroke="#33a6d7" stroke-width="3">
        <path d="M474 140A178 178 0 0 1 726 140"/>
        <path d="M726 140A178 178 0 0 1 726 392"/>
        <path d="M726 392A178 178 0 0 1 474 392"/>
        <path d="M474 392A178 178 0 0 1 474 140"/>
      </g>
      <g fill="#33a6d7">
        <rect x="466" y="132" width="16" height="16"/>
        <rect x="718" y="132" width="16" height="16"/>
        <rect x="718" y="384" width="16" height="16"/>
        <rect x="466" y="384" width="16" height="16"/>
      </g>
      <g fill="none" stroke="#33a6d7" stroke-width="2">
        <path d="M530 216A86 86 0 0 1 650 196"/>
        <path d="M670 216A86 86 0 0 1 650 336"/>
        <path d="M670 316A86 86 0 0 1 550 336"/>
        <path d="M530 316A86 86 0 0 1 550 196"/>
      </g>
      <g fill="#33a6d7">
        <path d="m650 196-2 9 8-5z"/>
        <path d="m650 336 9 2-5-8z"/>
        <path d="m550 336 2-9-8 5z"/>
        <path d="m550 196-9-2 5 8z"/>
      </g>
      <circle cx="600" cy="266" r="68" fill="#0255a3"/>
      <text x="600" y="283" text-anchor="middle" font-family="Lato, Arial, sans-serif" font-weight="700" font-size="46" fill="#ffffff">HSA</text>
    </svg>

    <div class="q-label" style="left:454px;top:1561px">How to<br>get<br>there?</div>
    <div class="q-label" style="left:626px;top:1554px">Where<br>are<br>we<br>now?</div>
    <div class="q-label" style="left:450px;top:1696px">Where<br>should<br>we get to?</div>
    <div class="q-label" style="left:652px;top:1696px">Where<br>could<br>we get to?</div>

    <ul class="process-list" style="left:186px;top:1452px;width:180px">
      <li>Develop plan and raodmap based on people, process, customer &amp; technology</li>
    </ul>
    <ul class="process-list" style="left:802px;top:1438px;width:260px">
      <li>Vision, mission, values &amp; strategic goals</li>
      <li>Services diagnostic</li>
      <li>Current offered</li>
      <li>Delivery model deployed</li>
      <li>Technology deployed</li>
    </ul>
    <ul class="process-list" style="left:186px;top:1726px;width:180px">
      <li>Strategic options agreed and prioritied based strategic goals, interview outcomes, best practice and busniess goals</li>
    </ul>
    <ul class="process-list" style="left:802px;top:1767px;width:200px">
      <li>SWOT analysis</li>
      <li>Comparison to best practise</li>
      <li>Comparison to competitors</li>
    </ul>
  </section>

  <section class="result" role="img" aria-label="Photo of a tablet showing charts in front of faded revenue, growth and profit bar charts">
    <h2 class="section-title" style="top:34px;font-weight:400">Process <span>Result</span></h2>
    <div class="title-rule" style="top:86px"></div>
    <div class="title-dot" style="top:86px"></div>
    <div class="bar" style="top:139px"><b style="width:75%;background:repeating-linear-gradient(135deg,#0255a3 0 6px,#0a5fae 6px 12px)">Customer Satisfaction 75%</b></div>
    <div class="bar" style="top:187px"><b style="width:50%;background:var(--sky)">Omni Channel Capability 50%</b></div>
    <div class="bar" style="top:235px"><b style="width:70%;background:var(--mid)">Workplace Planning 70%</b></div>
    <div class="bar" style="top:283px"><b style="width:79%;background:var(--cyan)">Self Service Maturity 79%</b></div>
    <div class="bar" style="top:331px"><b style="width:51%;background:var(--navy)">Analytics &amp; Reporting 51%</b></div>
  </section>

  <footer class="site-footer">
    <div class="notch" style="top:0;border-top:14px solid #e6e6e6"></div>
    <h4 class="foot-head" style="left:133px">Quick Links</h4>
    <ul class="foot-links">
      <li>Home</li><li>Services</li><li>Partners</li><li>Blog</li><li>Get in Touch</li>
    </ul>

    <h4 class="foot-head" style="left:293px">Contact Details</h4>
    <div class="contact-row" style="top:68px">
      <svg width="14" height="18" viewBox="0 0 14 18"><path d="M7 1a6 6 0 0 1 6 6c0 4-6 10-6 10S1 11 1 7a6 6 0 0 1 6-6z" fill="#fff"/><circle cx="7" cy="7" r="2" fill="#0b4c8c"/></svg>
      <span>Lorem ipsum dolor sit consectetuer<br>adipiscing elit, diam nonummy nibh<br>Quay Lane 12, Postcode: 40218</span>
    </div>
    <div class="contact-row" style="top:150px">
      <svg width="14" height="16" viewBox="0 0 14 16"><path d="M3 1c1 0 2 2 2 3s-1 1-1 2c1 2 2 3 4 4 1 0 1-1 2-1s3 1 3 2-2 3-3 3C5 14 1 9 1 4c0-1 1-3 2-3z" fill="#fff"/></svg>
      <span>555-207-4418</span>
    </div>
    <div class="contact-row" style="top:190px">
      <svg width="14" height="12" viewBox="0 0 14 12"><rect x="0" y="1" width="14" height="10" fill="#fff"/><path d="m0 1 7 6 7-6" fill="none" stroke="#0b4c8c" stroke-width="1.5"/></svg>
      <span>hello@harbourlineallies.test</span>
    </div>

    <h4 class="foot-head" style="left:580px">Recent Tweets</h4>
    <span class="abs" style="left:812px;top:30px;font-size:15px">&lsaquo; &rsaquo;</span>
    <div class="tweet" style="top:70px">
      <div class="avatar"></div>
      <div><strong>@harbourlineallies</strong><br>Lorem ipsum dolor sit consectetuer<br>adipiscing elit<time>15 hours ago</time></div>
    </div>
    <div class="tweet" style="top:150px">
      <div class="avatar"></div>
      <div><strong>@harbourlineallies</strong><br>Lorem ipsum dolor sit consectetuer<br>adipiscing elit<time>15 hours ago</time></div>
    </div>

    <div class="foot-divider"></div>
    <div class="foot-brand">HSA</div>
    <div class="follow">Follow Us On</div>
    <div class="socials"><span></span><span></span><span></span><span></span></div>
  </footer>
  <div class="copyright">Copyright &copy; 2015 Harbourline Service Allies. All Rights Reserved.</div>

</div>
</body>
</html>
```